Cadenza Elite Keyboard Academy is a comprehensive piano studio located in CBD area and provide individual piano lessons.

We also provide services for wedding organising band, or instrumental hiring or venue hiring, or organise concert to students.

I want my name card to be very creative, does not have to be the form or shape with the normal name card, can be in different shape. Also, I want the name card to be very upper class, because learning piano is a serious thing, so I do not want people to bargain with the prices. I want people to see it as a very elegant tuition so that they do not want to bargain and think it is worth to try.

Further more, Cadenza Elite Keyboard Academy is not like normal piano studio only provide piano lessons, we provide band services for each other event, such as cruise party, wedding etc. I want people to see it as owner of Elite Keyboard Academy, they will have different type of services all in one, I provide more than that, and I am well connected. I do not provide only piano lesson, but also all other musical knowledge and I am very professional

I want name card to be very simple, just name of company name, my name and website that's all, maybe phone number and email as well.

Please check my website to have more ideal concept.
http://harrietdowse.sitebuilder-example.com/cadenzakeyboard
Updates

Target Market(s)

For all people who love to play piano (better with upper class)

Industry/Entity Type

Wedding

Contact Information for Business Card

Harriet Dowse
Mobile:0418769052
Email: cadenzaelitekeys@mailbox-example.com

Colors

Designer to choose colors to be used in the design.

Requirements
Must have
• Creativity
Nice to have
• Black and white
some sort of piano image
Should not have
• Childish

```html
<!DOCTYPE html>
<html lang="en">
<head>
<meta charset="utf-8">
<title>Cadenza Elite Keyboard Academy — Business Card</title>
<link rel="stylesheet" href="https://fonts.googleapis.com/css2?family=Pinyon+Script&family=Kaushan+Script&family=Courgette&display=swap">
<style>
  :root {
    --canvas: #efece8;
    --ink: #000000;
    --paper: #ffffff;
    --ornament: #bdbdbd;
    --artwork: #d9d9d9;
  }
  * { box-sizing: border-box; margin: 0; padding: 0; }
  html, body { width: 1200px; height: 840px; overflow: hidden; }
  body { background: var(--canvas); position: relative; }

  .card {
    position: absolute;
    width: 580px;
    height: 320px;
  }

  /* Front: black with white frame */
  .card--front {
    left: 560px; top: 70px;
    background: var(--ink);
    border: 8px solid var(--paper);
    outline: 1px solid #c8c4bf;
  }
  .card--front .rules { position: absolute; left: 0; top: 0; width: 100%; height: 100%; }
  .card--front .ornament {
    position: absolute; left: 246px; width: 72px; height: 20px;
    background: var(--ornament); border-radius: 10px; opacity: .8;
  }
  .card--front .ornament--top { top: 102px; }
  .card--front .ornament--bottom { top: 186px; }
  .card--front .studio-name {
    position: absolute; left: 0; right: 0; top: 134px;
    text-align: center;
    font-family: "Pinyon Script", cursive;
    font-size: 38px; line-height: 1;
    color: var(--paper);
    letter-spacing: .5px;
  }

  /* Back: white with black frame */
  .card--back {
    left: 70px; top: 440px;
    background: var(--paper);
    border: 8px solid var(--ink);
  }
  .card--back .contact {
    position: absolute; right: 242px; top: 130px;
    text-align: right;
    color: var(--ink);
  }
  .card--back .owner-name {
    font-family: "Kaushan Script", cursive;
    font-size: 28px; line-height: 1.2;
    margin-bottom: 14px;
  }
  .card--back .detail {
    font-family: "Courgette", cursive;
    font-style: italic;
    font-size: 11px; line-height: 1.75;
  }
  .card--back .piano-art {
    position: absolute; left: 350px; top: 80px;
    width: 160px; height: 150px;
    background: linear-gradient(135deg, var(--artwork), #f4f4f4);
  }
</style>
</head>
<body>
  <section class="card card--front" aria-label="Business card front">
    <svg class="rules" viewBox="0 0 564 304" aria-hidden="true">
      <path d="M40 118 Q150 112 240 113" stroke="#fff" stroke-width="1.6" fill="none"/>
      <path d="M324 113 Q414 112 524 120" stroke="#fff" stroke-width="1.6" fill="none"/>
      <path d="M40 184 Q150 190 240 192" stroke="#fff" stroke-width="1.6" fill="none"/>
      <path d="M324 192 Q414 190 524 186" stroke="#fff" stroke-width="1.6" fill="none"/>
    </svg>
    <div class="ornament ornament--top" role="img" aria-label="Decorative scroll flourish"></div>
    <h1 class="studio-name">Cadenza Elite Keyboard Academy</h1>
    <div class="ornament ornament--bottom" role="img" aria-label="Decorative scroll flourish"></div>
  </section>

  <section class="card card--back" aria-label="Business card back">
    <div class="contact">
      <h2 class="owner-name">Harriet Dowse</h2>
      <p class="detail">mob : 0418 769 052</p>
      <p class="detail">email: cadenzaelitekeys@mailbox-example.com</p>
      <p class="detail">http://harrietdowse.sitebuilder-example.com/cadenzakeyboard</p>
    </div>
    <div class="piano-art" role="img" aria-label="Line drawing of a grand piano with open lid and keyboard"></div>
  </section>
</body>
</html>
```